Einladungskarten für Firmenjubiläum
Zielgruppe
Ich brauche eine digitale Einladungskarte zum 10-jährigen Firmenjubiläum, das am 12. Juli stattfinden soll. Zu uns; wir sind ein Ingenieurbüro im Bereich Digitalisierung und sicherheitskritische Systeme, wie sie in Flugzeugen, medizinischen Geräten, modernen Autos etc. vorkommen. Autonomes Fahren und Raumfahrtmedizin, sowie Fahrzeugsicherheit und Cyber-Sicherheit gehören z. B. zu unseren Schwerpunktthemen.
Aufgabenstellung
Ich bin für Ideen offen, die sich an dem Inhalt unserer Website anlehnen.

```html
<!DOCTYPE html>
<html lang="de">
<head>
<meta charset="utf-8">
<title>Einladung – 10 Jahre Veltrion Systems GmbH</title>
<link rel="stylesheet" href="https://fonts.googleapis.com/css2?family=Jost:wght@300;400;500;600&family=Chakra+Petch:wght@600&family=Exo+2:wght@200;300&family=Mrs+Saint+Delafield&display=swap">
<style>
  :root {
    --stage: #0b1d30;
    --card-top: #040608;
    --card-mid: #061524;
    --card-low: #0a3a66;
    --glow: #1f8fe0;
    --line: #2b9fe8;
    --neon: #35b4ff;
    --white: #ffffff;
    --soft: #e8f1fa;
    --band: #0d4a72;
  }
  html, body {
    margin: 0; padding: 0;
    width: 1000px; height: 1200px;
    overflow: hidden;
    background: var(--stage);
  }
  .invitation {
    position: absolute;
    left: 174px; top: 139px;
    width: 652px; height: 922px;
    overflow: hidden;
    background:
      radial-gradient(ellipse 70% 45% at 50% 72%, rgba(20,90,150,.55), transparent 70%),
      linear-gradient(180deg, var(--card-top) 0%, var(--card-top) 30%, var(--card-mid) 52%, var(--card-low) 100%);
    font-family: "Jost", sans-serif;
    color: var(--white);
  }
  .brand {
    position: absolute;
    top: 70px; left: 0; width: 100%;
    display: flex; align-items: center; justify-content: center; gap: 14px;
  }
  .brand-mark {
    width: 34px; height: 34px;
    background: var(--glow);
  }
  .brand-name {
    font-family: "Jost", sans-serif;
    font-weight: 500;
    font-size: 30px;
    letter-spacing: 3px;
    color: var(--white);
    line-height: 1;
  }
  .anniversary {
    position: absolute;
    left: 170px; top: 208px;
    width: 350px; height: 145px;
  }
  .years-band {
    position: absolute;
    left: 317px; top: 294px;
    width: 200px; height: 46px;
    background: linear-gradient(90deg, rgba(13,74,114,.2), var(--band) 25%, var(--band) 75%, rgba(13,74,114,0));
  }
  .years {
    position: absolute;
    left: 340px; top: 292px;
    font-family: "Exo 2", sans-serif;
    font-weight: 300;
    font-size: 33px;
    letter-spacing: .5px;
    color: var(--white);
  }
  .message {
    position: absolute;
    top: 397px; left: 90px; width: 472px;
    margin: 0;
    text-align: center;
    font-weight: 300;
    font-size: 18.5px;
    line-height: 27.5px;
    color: var(--soft);
  }
  .event-date, .event-place {
    position: absolute;
    left: 0; width: 100%;
    margin: 0;
    text-align: center;
    font-weight: 600;
    font-size: 19px;
  }
  .event-date { top: 521px; }
  .event-place { top: 565px; letter-spacing: .3px; }
  .divider {
    position: absolute;
    left: 100px; top: 551px;
    width: 456px; height: 10px;
  }
  .signature {
    position: absolute;
    top: 630px; left: 0; width: 100%;
    text-align: center;
    font-family: "Mrs Saint Delafield", cursive;
    font-size: 44px;
    color: var(--white);
  }
  .globe-scene {
    position: absolute;
    left: 0; bottom: 0;
    width: 652px; height: 250px;
    background:
      radial-gradient(ellipse 60% 90% at 50% 100%, rgba(40,150,230,.75), rgba(20,100,180,.35) 60%, transparent 80%);
  }
</style>
</head>
<body>
  <main class="invitation">
    <header class="brand">
      <span class="brand-mark"></span>
      <span class="brand-name">VELTRION SYSTEMS GmbH</span>
    </header>

    <div class="years-band"></div>
    <svg class="anniversary" viewBox="0 0 350 145" aria-label="10 Jahre">
      <text x="0" y="140" fill="var(--neon)" font-family="Exo 2, sans-serif" font-weight="200" font-size="196" textLength="150" lengthAdjust="spacingAndGlyphs">10</text>
      <text x="195" y="73" fill="var(--neon)" font-family="Chakra Petch, sans-serif" font-weight="600" font-size="60" letter-spacing="1" textLength="157" lengthAdjust="spacingAndGlyphs">JAHRE</text>
    </svg>
    <div class="years">2014-2024</div>

    <p class="message">Wir laden Sie herzlich dazu ein, unser 10-jähriges Firmenbestehen zu feiern und gemeinsam auf weitere erfolgreiche Jahre anzustoßen</p>

    <p class="event-date">Dienstag, 20.6.2024 um 18:00 Uhr</p>
    <svg class="divider" viewBox="0 0 456 10" aria-hidden="true">
      <line x1="4" y1="5" x2="452" y2="5" stroke="var(--line)" stroke-width="1.5"/>
      <circle cx="4" cy="5" r="3.5" fill="var(--neon)"/>
      <circle cx="278" cy="5" r="3" fill="var(--neon)"/>
      <circle cx="452" cy="5" r="3.5" fill="var(--neon)"/>
    </svg>
    <p class="event-place">Muster Street 12 2398 Musterstadt Germany</p>

    <div class="signature">Veltrion Systems GmbH</div>

    <div class="globe-scene" role="img" aria-label="Illustration: vernetzte Weltkugel aus Lichtpunkten mit zwei Satelliten im Orbit"></div>
  </main>
</body>
</html>
```